Varnecke Holdings Webpage Design

We need a new website for our company. The company is Varnecke Holdings Pty Ltd. We are in the business of Asbestos Removal; Demolition; Earthworks and Transport. We do not advertise and would like our website to be a reference point for our clients / potential clients and also to make our services known to those searching the internet for the services we offer. Some examples of the style of website we are after are:
http://www.quillmarkwrecking.example.au/
http://m.tovrinbrookclearing.example.au/
http://www.pellowayclearance.example.au
http://www.zorvat.example.au
http://www.kjbworks.example.au
http://www.northpeak-dismantling.example.au
We will need to work on content. Enclosed is an example. We also need to purchase the domain varneckeholdings.example.au and need to set up email accounts and ensure the website is mobile friendly. We have a company logo and have built our business on delivering professional, quality services on time. We would like the webpage to be simple, informative and professional - black and white / grey themed. We would also like to add a photo gallery etc later.

Colors
000000
fcfcfc
959595
dddddd

Requirements
Must have
• Information regarding the services we provide

```html
<!DOCTYPE html>
<html lang="en">
<head>
<meta charset="utf-8">
<title>Varnecke Holdings</title>
<link href="https://fonts.googleapis.com/css2?family=Exo+2:wght@300;400;600&family=Open+Sans:wght@400;700&family=Raleway:wght@400;500&display=swap" rel="stylesheet">
<style>
:root{
  --black:#000000;
  --white:#fcfcfc;
  --grey:#959595;
  --light:#dddddd;
  --ink:#1a1a1a;
  --body:#555555;
  --footer:#231f20;
  --nav-active:#5e5e5e;
}
*{margin:0;padding:0;box-sizing:border-box}
html,body{width:1200px;height:2514px;overflow:hidden;background:var(--white)}
body{position:relative;font-family:"Open Sans",sans-serif;color:var(--ink)}
.abs{position:absolute}

/* header */
.brand{left:77px;top:34px;font-family:"Exo 2",sans-serif;font-weight:400;font-size:40px;letter-spacing:6px;color:#333;line-height:50px}
.phone{left:864px;top:37px;display:flex;align-items:center;gap:18px}
.phone-ring{width:62px;height:62px;border:2px solid #444;border-radius:50%;display:flex;align-items:center;justify-content:center}
.phone-num{font-family:"Open Sans",sans-serif;font-weight:700;font-size:28px;color:var(--black)}

/* hero */
.hero{left:0;top:152px;width:1200px;height:614px;background:linear-gradient(180deg,#6d8fb4 0%,#9fb3c7 38%,#b6a690 58%,#8a7864 80%,#6c5a48 100%)}
.hero-machine{left:80px;top:240px;width:470px;height:260px;border-radius:6px;background:radial-gradient(ellipse at 45% 50%,#d6b23a 0%,#a88a2e 55%,rgba(120,100,60,0) 75%)}
.nav{left:77px;top:121px;width:1046px;height:62px;background:var(--black);display:flex}
.nav a{font-family:"Raleway",sans-serif;font-size:21px;color:var(--white);text-decoration:none;display:flex;align-items:center;justify-content:center;height:62px;letter-spacing:.5px}
.nav a.active{background:var(--nav-active)}

.quote{left:766px;top:253px;width:357px;height:426px;background:rgba(0,0,0,.82);padding:0 24px}
.quote h2{font-family:"Exo 2",sans-serif;font-weight:400;font-size:28px;color:var(--white);text-align:center;margin-top:20px;letter-spacing:.5px}
.field{width:310px;height:35px;background:var(--white);margin-top:17px;font-family:"Open Sans",sans-serif;font-size:15px;color:#777;padding:6px 12px}
.quote h2+.field{margin-top:14px}
.field.area{height:72px}
.btn{display:block;margin:17px auto 0;width:156px;height:40px;background:var(--black);color:var(--white);font-family:"Raleway",sans-serif;font-size:21px;text-align:center;line-height:40px}

/* welcome */
.h-section{left:0;width:1200px;text-align:center;font-family:"Exo 2",sans-serif;font-weight:300;font-size:37px;letter-spacing:1px;color:var(--ink)}
.h-section b{font-weight:600;letter-spacing:2px}
.lead{left:184px;width:832px;text-align:center;font-size:16px;line-height:25px;color:var(--body)}

.service{top:996px;width:235px;text-align:center}
.service .pic{height:134px}
.service h3{font-family:"Raleway",sans-serif;font-weight:500;font-size:23px;margin-top:20px;color:var(--ink)}
.service p{font-size:15.5px;line-height:25px;color:var(--body);margin:8px auto 0;width:200px}

/* testimonial */
.band{left:0;top:1341px;width:1200px;height:375px;background:linear-gradient(180deg,#3a3a3a 0%,#2b2b2b 60%,#1e1e1e 100%)}
.band-title{left:0;top:1396px;width:1200px;text-align:center;font-family:"Exo 2",sans-serif;font-weight:300;font-size:36px;color:var(--white)}
.band-text{left:215px;top:1520px;width:770px;text-align:center;font-size:16px;line-height:25px;color:var(--light)}
.band-name{left:0;top:1608px;width:1200px;text-align:center;font-size:15px;font-weight:700;color:var(--white)}
.arrow{width:56px;height:56px;border:2px solid var(--white);border-radius:50%;display:flex;align-items:center;justify-content:center}

/* projects */
.project{top:1914px;width:334px;height:221px}

/* footer */
.footer{left:0;top:2200px;width:1200px;height:314px;background:var(--footer)}
.f-head{top:2222px;font-family:"Raleway",sans-serif;font-size:23px;color:var(--white)}
.f-list{left:85px;top:2264px;list-style:none;font-size:15px;color:var(--white);line-height:31px}
.f-list li::before{content:"";display:inline-block;width:6px;height:6px;background:var(--white);border-radius:50%;margin-right:10px;vertical-align:middle}
.f-divider{top:2229px;width:1px;height:210px;background:#4a4647}
.f-row{left:446px;display:flex;gap:18px;font-size:15px;color:var(--white);line-height:24px}
.f-row svg{flex:none;margin-top:2px}
.social{left:811px;top:2272px;display:flex;gap:44px}
.social span{width:18px;height:18px;border:2px solid var(--white);border-radius:50%}
.f-brand{left:811px;top:2334px;font-family:"Exo 2",sans-serif;font-weight:400;font-size:28px;letter-spacing:3px;color:#5a5657}
.f-rule{left:77px;top:2459px;width:1046px;height:1px;background:#4a4647}
.copy{left:0;top:2475px;width:1200px;text-align:center;font-size:15px;color:var(--grey)}
.copy b{color:var(--white)}
</style>
</head>
<body>

<header>
  <div class="abs brand">VARNECKE HOLDINGS</div>
  <div class="abs phone">
    <div class="phone-ring">
      <svg width="30" height="30" viewBox="0 0 24 24"><path fill="#333" d="M6.6 10.8c1.4 2.8 3.8 5.1 6.6 6.6l2.2-2.2c.3-.3.7-.4 1-.2 1.1.4 2.3.6 3.6.6.6 0 1 .4 1 1V20c0 .6-.4 1-1 1C10.6 21 3 13.4 3 4c0-.6.4-1 1-1h3.5c.6 0 1 .4 1 1 0 1.3.2 2.5.6 3.6.1.3 0 .7-.2 1z"/></svg>
    </div>
    <div class="phone-num">0491 570 156</div>
  </div>
</header>

<section>
  <div class="abs hero" role="img" aria-label="Photo of a yellow bulldozer working on a rocky earthworks site under a cloudy sky"></div>
  <div class="abs hero-machine" role="img" aria-label="Yellow bulldozer"></div>
  <nav class="abs nav">
    <a class="active" href="#" style="width:131px">HOME</a>
    <a href="#" style="width:137px">ABOUT</a>
    <a href="#" style="width:150px">SERVICES</a>
    <a href="#" style="width:136px">SAFETY</a>
    <a href="#" style="width:205px">ENVIRONMENT</a>
    <a href="#" style="width:140px">CONTACT</a>
  </nav>
  <form class="abs quote">
    <h2>GET A FREE QUOTE</h2>
    <div class="field">Enter Name</div>
    <div class="field">Enter Company Name</div>
    <div class="field">Contact No.</div>
    <div class="field">Email Id</div>
    <div class="field area">Details</div>
    <span class="btn">GET QUOTE</span>
  </form>
</section>

<section>
  <h1 class="abs h-section" style="top:810px">WELCOME TO <b>VARNECKE HOLDINGS</b></h1>
  <p class="abs lead" style="top:872px">Varnecke Transport Pty Ltd was established by Director Martin Varnecke in 2002 with a focus providing services within the transport industry. Over time the company has developed and expanded to include the provision of Earthworks and Demolition.</p>

  <div class="abs service" style="left:77px">
    <div class="pic" role="img" aria-label="Excavator breaking concrete on a demolition site" style="background:linear-gradient(160deg,#5f95c8,#a9b6bc 50%,#8d8a80)"></div>
    <h3>Demolition</h3>
    <p>Varnecke Transport and Demolition provide an extensive range of demolition services.</p>
  </div>
  <div class="abs service" style="left:349px">
    <div class="pic" role="img" aria-label="Wheel loader with raised bucket on an earthworks site" style="background:linear-gradient(160deg,#6f8fa6,#7a6d55 55%,#3f3a30)"></div>
    <h3>Earthworks</h3>
    <p>Varnecke Transport and Demolition possess all necessary equipment and skilled personnel...</p>
  </div>
  <div class="abs service" style="left:618px">
    <div class="pic" role="img" aria-label="Corrugated asbestos roof sheeting beside green foliage" style="background:linear-gradient(170deg,#9cbad0,#7d9a62 40%,#b9b8b2 65%,#8f8e88)"></div>
    <h3>Asbestos</h3>
    <p>Asbestos is a naturally occurring silicate mineral made up of tiny fibres.</p>
  </div>
  <div class="abs service" style="left:888px">
    <div class="pic" role="img" aria-label="Yellow excavator digging on a sandy site under blue sky" style="background:linear-gradient(160deg,#4b8ccf,#a9c4dc 45%,#c9a660 75%,#9c7b45)"></div>
    <h3>Hours of Operation</h3>
    <p>Varnecke Transport and Demolition operate Monday to Saturday.</p>
  </div>
</section>

<section>
  <div class="abs band" role="img" aria-label="Greyscale photo of a construction site with tower cranes"></div>
  <h2 class="abs band-title">WHAT OUR CLIENT SAY</h2>
  <svg class="abs" style="left:582px;top:1470px" width="36" height="30" viewBox="0 0 36 30"><path fill="#fcfcfc" d="M0 30V17C0 7 5 1 14 0v6c-4 1-6 4-6 9h6v15zM22 30V17c0-10 5-16 14-17v6c-4 1-6 4-6 9h6v15z"/></svg>
  <p class="abs band-text">Lorem Ipsum is simply dummy text of the printing and typesetting industry. Lorem Ipsum has been the industry's standard dummy text ever since the 1500s, when an unknown printer took a galley of type and scrambled it to make a type specimen book.</p>
  <div class="abs band-name">- Client Name</div>
  <div class="abs arrow" style="left:78px;top:1537px"><svg width="18" height="22" viewBox="0 0 18 22"><path d="M13 2L4 11l9 9" fill="none" stroke="#fcfcfc" stroke-width="4"/></svg></div>
  <div class="abs arrow" style="left:1066px;top:1537px"><svg width="18" height="22" viewBox="0 0 18 22"><path d="M5 2l9 9-9 9" fill="none" stroke="#fcfcfc" stroke-width="4"/></svg></div>
</section>

<section>
  <h2 class="abs h-section" style="top:1764px">OUR PROJECT</h2>
  <p class="abs lead" style="top:1826px">Lorem Ipsum is simply dummy text of the printing and typesetting industry. Lorem Ipsum has been the industry's standard dummy text ever since the 1500s.</p>
  <div class="abs project" style="left:77px" role="img" aria-label="Excavator breaking concrete on a demolition site" style="background:#888"></div>
  <div class="abs project" style="left:77px;background:linear-gradient(160deg,#5f95c8,#a9b6bc 50%,#8d8a80)" role="img" aria-label="Excavator breaking concrete on a demolition site"></div>
  <div class="abs project" style="left:432px;background:linear-gradient(160deg,#4b8ccf,#a9c4dc 45%,#c9a660 75%,#9c7b45)" role="img" aria-label="Yellow excavator digging on a sandy site"></div>
  <div class="abs project" style="left:789px;background:linear-gradient(160deg,#6f8fa6,#7a6d55 55%,#3f3a30)" role="img" aria-label="Wheel loader with raised bucket on an earthworks site"></div>
</section>

<footer>
  <div class="abs footer"></div>
  <h4 class="abs f-head" style="left:79px">Useful Links</h4>
  <ul class="abs f-list">
    <li>Home</li><li>About</li><li>Services</li><li>Safety</li><li>Environment</li><li>Contact</li>
  </ul>
  <div class="abs f-divider" style="left:416px"></div>
  <div class="abs f-divider" style="left:783px"></div>

  <h4 class="abs f-head" style="left:446px">Conact Us</h4>
  <div class="abs f-row" style="top:2266px">
    <svg width="14" height="20" viewBox="0 0 14 20"><path fill="#fcfcfc" d="M7 0C3 0 0 3 0 7c0 5 7 13 7 13s7-8 7-13c0-4-3-7-7-7zm0 10a3 3 0 110-6 3 3 0 010 6z"/></svg>
    <span>PO Box 112 KELDARRA QLD 4999</span>
  </div>
  <div class="abs f-row" style="top:2306px">
    <svg width="20" height="20" viewBox="0 0 24 24"><path fill="#fcfcfc" d="M6.6 10.8c1.4 2.8 3.8 5.1 6.6 6.6l2.2-2.2c.3-.3.7-.4 1-.2 1.1.4 2.3.6 3.6.6.6 0 1 .4 1 1V20c0 .6-.4 1-1 1C10.6 21 3 13.4 3 4c0-.6.4-1 1-1h3.5c.6 0 1 .4 1 1 0 1.3.2 2.5.6 3.6.1.3 0 .7-.2 1z"/></svg>
    <span>0491 570 156<br>0491 570 110</span>
  </div>
  <div class="abs f-row" style="top:2367px">
    <svg width="20" height="16" viewBox="0 0 20 16"><rect x="1" y="1" width="18" height="14" fill="none" stroke="#fcfcfc" stroke-width="2"/><path d="M1 1l9 8 9-8" fill="none" stroke="#fcfcfc" stroke-width="2"/></svg>
    <span>vhdemolition@mail.example.au</span>
  </div>

  <h4 class="abs f-head" style="left:811px">Follow Us</h4>
  <div class="abs social"><span></span><span></span><span></span></div>
  <div class="abs f-brand">VARNECKE HOLDINGS</div>

  <div class="abs f-rule"></div>
  <div class="abs copy">© <b>VARNECKE HOLDINGS</b> - 2015. All Rights Reserved.</div>
</footer>

</body>
</html>
```